Mossy Den Pet Supply

Thank you for your interest in this design contest. We are always welcome to questions and are looking forward to seeing what you can come up with.

We work on a Bootstrap platform with our custom built CMS. We require all designs to be sized accordingly with the bootstrap grid system found here: http://fernlattice.com/css/#grid

At the start of a competition, we are looking for general Home Page Design concepts and an example product grid page.

Homepage: Slide Show/Featured Products/Specials

example website as a reference:https://www.mintcollarworks.com/

Store Product Grid: Show a grid of product thumbnails. Included elements are thumbnail and price. Also included are filters (sort by, show by grid/list).

No photos at this time but Logo is attached. Looking for good quality photo's around the web. Please read the attached creative brief in depth to get an idea f what the client is looking for. Thanks!

```html
<!DOCTYPE html>
<html lang="en">
<head>
<meta charset="utf-8">
<title>Mossy Den Pet Supply</title>
<link href="https://fonts.googleapis.com/css2?family=Arimo:wght@400;700&display=swap" rel="stylesheet">
<style>
:root{
  --green:#8dc63f;
  --green-dark:#6a9e1f;
  --text:#666;
  --text-dark:#555;
  --nav:#666;
  --page:#f8f8f8;
  --dot:#d9a441;
}
*{margin:0;padding:0;box-sizing:border-box}
html,body{width:990px;height:1200px;overflow:hidden;background:var(--page)}
body{font-family:"Arimo",Arial,sans-serif;color:var(--text);position:relative}
.abs{position:absolute}
.top-rule{left:0;top:0;width:990px;height:4px;background:var(--green)}
.header{left:0;top:4px;width:990px;height:98px;background:linear-gradient(#f6f6f6,#ececec)}
.brand{display:flex;align-items:center;gap:6px;font-weight:700;font-size:14px;line-height:16px;color:#222;text-transform:uppercase}
.brand-mark{width:14px;height:14px;background:var(--green)}
.site-brand{left:132px;top:36px}
.nav{top:60px;left:427px;display:flex;align-items:center;font-size:12.5px;letter-spacing:.6px;color:var(--nav)}
.nav a{color:inherit;text-decoration:none;margin-right:28px}
.nav .active{background:var(--green);color:#fff;padding:3px 9px;box-shadow:-3px 3px 0 #3f6d10;margin-right:20px}
.hero{left:0;top:102px;width:990px;height:313px;background:linear-gradient(100deg,#9a5a3c 0%,#efe3dc 18%,#f7efe9 40%,#d79a7c 60%,#f1d2bd 78%,#f5ede6 100%)}
.pillars{left:128px;top:278px;width:246px;height:72px;border-top:1px dashed var(--green);border-bottom:2px dotted var(--green);display:flex}
.pillar{padding:8px 0 0 1px;width:85px;border-right:1px dashed var(--green);font-size:12.5px;line-height:16px;color:#333}
.pillar:last-child{border:0}
.pillar h3{color:var(--green);font-size:17px;font-weight:700;line-height:18px}
.events-banner{left:102px;top:421px;width:780px;height:48px}
.events-banner .label{position:absolute;left:36px;top:10px;font-size:22px;font-weight:700;color:#fff;letter-spacing:.8px;text-shadow:0 1px 1px #3f6d10}
.events-banner .ticker{position:absolute;left:245px;top:16px;font-size:13px;font-weight:700;color:#fff;letter-spacing:.6px}
.shop-strip{left:101px;top:487px;width:774px;height:138px;background:linear-gradient(#9ccf4c,#7db22e);box-shadow:0 1px 3px rgba(0,0,0,.35)}
.thumb{position:absolute;top:22px;width:163px;height:81px;border:1px solid #fff}
.thumb-label{position:absolute;top:111px;font-size:15px;font-weight:700;color:#fff;letter-spacing:1.3px;text-shadow:0 1px 1px #3f6d10}
.strip-arrow{position:absolute;top:52px;width:27px;height:27px}
.cta{left:117px;top:559px;width:246px;height:35px;background:linear-gradient(#9ccf4c,#6fa624);box-shadow:0 2px 3px rgba(0,0,0,.35);color:#fff;font-weight:700;font-size:15px;letter-spacing:1.2px;text-align:center;line-height:35px;text-shadow:0 1px 1px #3f6d10}
.col-title{font-size:17px;font-weight:700;color:var(--green)}
.body-text{font-size:11.6px;line-height:19.8px;color:var(--text);text-align:justify}
.body-text b{color:var(--text-dark)}
.date{font-size:12px;color:var(--green);margin-bottom:2px}
.event-item{padding-bottom:8px;margin-bottom:12px;border-bottom:1px dashed var(--dot)}
.event-item:last-child{border:0}
.events-col{left:124px;top:653px;width:182px}
.events-col .col-title{margin-bottom:10px}
.blog-col{left:327px;top:654px;width:358px}
.blog-row{display:flex;gap:12px;margin-top:6px}
.photo{flex:none}
.video-col{left:711px;top:653px;width:172px}
.video{width:170px;height:117px;background:#bbb;border:1px solid #aaa;padding:4px;margin-top:10px}
.video .screen{height:94px;background:linear-gradient(#d8d8d8,#1c1c1c 60%)}
.video .bar{height:11px;margin-top:2px;background:#e6e6e6;display:flex;align-items:center;gap:4px;padding:0 4px}
.connect-title{margin-top:16px}
.connect-list{list-style:none;margin-top:4px}
.connect-list li{display:flex;align-items:center;gap:10px;font-size:11.5px;letter-spacing:.6px;color:#555;height:28px}
.icon-box{width:17px;height:15px;background:var(--green);flex:none}
.footer{left:0;top:1064px;width:990px;height:136px;background:linear-gradient(#ededed,#f6f6f6);border-top:4px solid var(--green)}
.footer-brand{left:132px;top:1100px}
.footer-info{left:285px;top:1074px;font-size:10.5px;letter-spacing:.6px;line-height:22px;color:#555}
.footer-links{top:1074px;font-size:11.5px;line-height:22px;color:#555}
.copyright{left:408px;top:1173px;font-size:10.5px;letter-spacing:.6px;color:#555}
.dog-photo{left:770px;top:955px;width:220px;height:245px;background:radial-gradient(ellipse at 55% 55%,rgba(140,62,40,.55) 0%,rgba(140,62,40,.3) 45%,rgba(140,62,40,0) 72%)}
</style>
</head>
<body>
<div class="abs top-rule"></div>
<header class="abs header"></header>
<div class="abs brand site-brand"><span class="brand-mark"></span><span>Mossy Den<br>Pet Supply</span></div>
<nav class="abs nav">
  <a class="active">Dogs</a><a>Our story</a><a>The scoop</a><a>Find a retailer</a><a>Blog</a><a>Events</a>
</nav>

<div class="abs hero" role="img" aria-label="Close-up photo of a smiling woman hugging a white dog"></div>
<div class="abs pillars">
  <div class="pillar"><h3>Live</h3>Have fun<br>in your visit</div>
  <div class="pillar"><h3>Love</h3>Love for<br>the Dogs</div>
  <div class="pillar"><h3>Learn</h3>Get to know<br>accessories</div>
</div>

<div class="abs events-banner">
  <svg width="780" height="48" viewBox="0 0 780 48">
    <defs><linearGradient id="bannerGreen" x1="0" y1="0" x2="0" y2="1"><stop offset="0" stop-color="#9fd04d"/><stop offset="1" stop-color="#6fa624"/></linearGradient></defs>
    <polygon points="220,0 768,0 780,24 768,48 220,48" fill="#0c0c0c"/>
    <polygon points="0,0 220,0 232,24 220,48 0,48" fill="url(#bannerGreen)"/>
    <polyline points="6,5 222,5 231,24 222,43 6,43" fill="none" stroke="#fff" stroke-width="1" stroke-dasharray="3 3" opacity=".7"/>
    <polyline points="236,5 762,5 772,24 762,43 236,43" fill="none" stroke="#fff" stroke-width="1" stroke-dasharray="3 3" opacity=".6"/>
  </svg>
  <span class="label">Special Events:</span>
  <span class="ticker">Lorum ispum is simply a dummy text that is used in websites</span>
</div>

<section class="abs shop-strip">
  <div class="thumb" style="left:37px;background:linear-gradient(#3a2a22,#d9c9a9)" role="img" aria-label="Photo of a dog resting on a dog bed by a fireplace"></div>
  <div class="thumb" style="left:216px;background:linear-gradient(90deg,#d9cbb2,#e86060)" role="img" aria-label="Photo of plush toy dogs with red leashes"></div>
  <div class="thumb" style="left:395px;background:linear-gradient(#9a6b4a,#5a3b2a)" role="img" aria-label="Photo of a dog among colourful toys"></div>
  <div class="thumb" style="left:575px;background:linear-gradient(#e8ddcf,#cdbba4)" role="img" aria-label="Photo of a small white dog on a fluffy blanket"></div>
  <span class="thumb-label" style="left:62px">Dog Bedding</span>
  <span class="thumb-label" style="left:252px">Dog Leashes</span>
  <span class="thumb-label" style="left:437px">Dog Toy</span>
  <span class="thumb-label" style="left:614px">Dog Blanket</span>
  <svg class="strip-arrow" style="left:4px" viewBox="0 0 27 27"><circle cx="13.5" cy="13.5" r="12" fill="none" stroke="#fff" stroke-width="2"/><polyline points="16,7 9,13.5 16,20" fill="none" stroke="#fff" stroke-width="2.5"/></svg>
  <svg class="strip-arrow" style="left:743px" viewBox="0 0 27 27"><circle cx="13.5" cy="13.5" r="12" fill="none" stroke="#fff" stroke-width="2"/><polyline points="11,7 18,13.5 11,20" fill="none" stroke="#fff" stroke-width="2.5"/></svg>
</section>
<div class="abs cta">Buy Dog Accessories</div>

<section class="abs events-col">
  <h2 class="col-title">Events</h2>
  <div class="event-item"><p class="date">April 13</p><p class="body-text"><b>Lorem Ipsum is simply dummy text of the</b> printing and typesetting industry. Lorem Ipsum</p></div>
  <div class="event-item"><p class="date">May 13</p><p class="body-text"><b>Lorem Ipsum is simply dummy text of the printing and typeset-ting</b> Ipsum has been the industry's standard dummy</p></div>
  <div class="event-item"><p class="date">April 30</p><p class="body-text"><b>Lorem Ipsum is simply dummy text of the printing and typeset-ting</b> Ipsum has been the industry's standard dummy</p></div>
</section>

<section class="abs blog-col">
  <h2 class="col-title">Blog : Lorum ipsum is dummy text</h2>
  <p class="body-text" style="margin-top:8px"><b>Lorem Ipsum is simply dummy text of the printing and typesetting industry.</b> Lorem Ipsum has been</p>
  <div class="blog-row">
    <div class="photo" style="width:163px;height:82px;margin-top:6px;background:linear-gradient(90deg,#d9cbb2,#e86060)" role="img" aria-label="Photo of plush toy dogs with red leashes"></div>
    <p class="body-text"><b>Lorem Ipsum is simply dummy text of the printing and typeset-ting industry.</b> Lorem Ipsum has been the industry's standard dummy text ever since the 1500s</p>
  </div>
  <div class="blog-row" style="margin-top:12px">
    <div class="photo" style="width:98px;height:81px;margin-top:4px;background:linear-gradient(#3a2a22,#d9c9a9)" role="img" aria-label="Photo of a dog on a dog bed by a fireplace"></div>
    <p class="body-text"><b>Lorem Ipsum is simply dummy text of the printing and typesetting industry.</b> Lorem Ipsum has been the industry's standard dummy text ever since the 1500s</p>
  </div>
  <p class="body-text" style="margin-top:4px"><b>Lorem Ipsum is simply dummy text of the printing and typeset-ting industry.</b> Lorem Ipsum has been the industry's standard dummy text ever since the 1500s.when an unknown printer took a galley of type and scrambled it to make a type specimen book</p>
</section>

<section class="abs video-col">
  <h2 class="col-title">Video Premiere</h2>
  <p class="body-text" style="margin-top:6px;line-height:15px;text-align:left"><b>Lorem Ipsum is simply dummy text of the</b> printing</p>
  <div class="video">
    <div class="screen" role="img" aria-label="Video still of a small white dog">
      <svg width="160" height="94" viewBox="0 0 160 94"><circle cx="80" cy="47" r="22" fill="none" stroke="#eee" stroke-width="4" opacity=".8"/><polygon points="73,36 73,58 91,47" fill="#eee" opacity=".85"/></svg>
    </div>
    <div class="bar">
      <svg width="6" height="7" viewBox="0 0 6 7"><polygon points="0,0 6,3.5 0,7" fill="#333"/></svg>
      <div style="flex:1;height:3px;background:linear-gradient(90deg,#c22 40%,#e99 40%)"></div>
      <svg width="7" height="7" viewBox="0 0 7 7"><polygon points="0,2 3,2 6,0 6,7 3,5 0,5" fill="#333"/></svg>
      <svg width="6" height="6" viewBox="0 0 6 6"><rect width="6" height="6" fill="#333"/></svg>
    </div>
  </div>
  <h2 class="col-title connect-title">Connect</h2>
  <ul class="connect-list">
    <li><svg width="17" height="13" viewBox="0 0 17 13"><rect width="17" height="13" fill="#8dc63f"/><polyline points="0,0 8.5,7 17,0" fill="none" stroke="#fff" stroke-width="1.5"/></svg>Email us</li>
    <li><span class="icon-box"></span>Pagebook</li>
    <li><span class="icon-box"></span>Chirper</li>
  </ul>
</section>

<div class="abs dog-photo" role="img" aria-label="Photo of a red setter dog carrying a stick"></div>

<footer class="abs footer"></footer>
<div class="abs brand footer-brand"><span class="brand-mark"></span><span>Mossy Den<br>Pet Supply</span></div>
<div class="abs footer-info">Ellentesque habitant morbi tristique<br>412 088-51 730 or 6104 3187 552<br>hello@mossydenpets.com</div>
<div class="abs footer-links" style="left:533px">Home<br>Our Story<br>Blog</div>
<div class="abs footer-links" style="left:623px">The Scoop<br>Events<br>Gallery</div>
<div class="abs copyright">Copyright © 2014 MOSSY DEN PET SUPPLY. All Rights Reserved.</div>
</body>
</html>
```